A revolutionary website for a revolutionary construction company

I am looking for inspirations... please help me and read the attached brief

I would like to achieve a website design that is modern, premium dynamic and drives emotions. I do not want a design that can be found on a normal template. Having that said, I would also like the utilisation of Illustrations that are relation to the company’s services…. Also would like to have illustrations dynamic when you navigate on them. So a young, dynamic and parallax design website that will show off these requirements. Also to add trust, with all pages designed.

please see attachements.
Updates

Low design quality

Target Market(s)

Please read brief

Number of Pages Required

5+ page

Font styles to use
Other font styles liked:
• Futura

Requirements
Must have
• Please read brief - colours to be matching logo colours
Nice to have
Should not have

```html
<!DOCTYPE html>
<html lang="en">
<head>
<meta charset="utf-8">
<title>ForgeLine Designs</title>
<link href="https://fonts.googleapis.com/css2?family=Poppins:wght@300;400;500;600;700&display=swap" rel="stylesheet">
<style>
:root{
  --crimson:#9d1a46;
  --crimson-band:#a8194b;
  --ink:#4b4447;
  --text:#5a5456;
  --muted:#8a8486;
  --rule:#e3e0e1;
  --footer:#5a4e52;
  --white:#ffffff;
  --star:#f0b43c;
}
*{box-sizing:border-box;margin:0;padding:0}
html,body{width:1200px;height:5213px;overflow:hidden}
body{position:relative;font-family:'Poppins',sans-serif;color:var(--text);background:var(--white)}
.abs{position:absolute}
.fill{position:absolute}
.btn{position:absolute;display:flex;align-items:center;justify-content:center;border-radius:23px;font-size:14px;font-weight:600;letter-spacing:.5px;text-transform:uppercase}
.btn-crimson{background:var(--crimson);color:var(--white)}
.btn-white{background:var(--white);color:var(--ink)}
.section-title{position:absolute;left:0;width:1200px;text-align:center;font-size:64px;font-weight:400;color:var(--ink);line-height:1}

/* header */
.brand{position:absolute;left:86px;top:56px;display:flex;align-items:center;gap:12px}
.brand-mark{width:70px;height:70px;border-radius:50%;border:2px solid var(--ink)}
.brand-name{font-size:14px;font-weight:600;color:var(--crimson);letter-spacing:3px}
.hero-photo{left:603px;top:0;width:597px;height:722px;background:linear-gradient(160deg,#7c7c7c 0%,#3d4145 35%,#8c6a4e 62%,#cfcac6 100%)}
.nav{position:absolute;left:522px;top:47px;width:589px;height:89px;background:var(--white);display:flex;align-items:center;justify-content:flex-end;padding-right:34px;gap:29px}
.nav a{font-size:13px;font-weight:500;color:var(--ink);text-decoration:none;text-transform:uppercase}
.nav a.active{color:var(--crimson);font-weight:600;border-bottom:2px solid var(--crimson);padding-bottom:4px}
.hero-title{left:81px;top:250px;font-size:98px;line-height:90px;font-weight:500;color:var(--ink)}
.hero-text{left:87px;top:470px;width:480px;font-size:15px;line-height:24px;color:var(--ink)}
.thumb-a{left:520px;top:652px;width:164px;height:139px;background:linear-gradient(180deg,#e8e7e5,#a9a6a2)}
.thumb-b{left:700px;top:652px;width:164px;height:139px;background:linear-gradient(180deg,#eeece8,#cfd3cf)}

/* about */
.about-panel{left:144px;top:897px;width:267px;height:520px;background:repeating-linear-gradient(135deg,#5a4f52 0 6px,#544a4d 6px 9px)}
.about-ring{left:211px;top:958px;width:396px;height:396px;border-radius:50%;background:var(--white);box-shadow:0 16px 40px rgba(0,0,0,.18)}
.about-photo{left:223px;top:970px;width:372px;height:372px;border-radius:50%;background:radial-gradient(circle at 55% 40%,#8fa2bb,#b89868 55%,#6e645c)}
.about-title{left:660px;top:970px;font-size:64px;font-weight:400;color:var(--ink)}
.about-text{left:658px;top:1057px;width:410px;font-size:15px;line-height:24px;color:var(--ink)}

/* services */
.service{position:absolute;top:1575px;width:300px;height:493px;color:var(--white);text-align:center}
.service .shade{position:absolute;inset:0;background:linear-gradient(180deg,rgba(0,0,0,0) 55%,rgba(40,30,35,.75) 100%)}
.service h3{position:absolute;left:0;right:0;bottom:84px;font-size:26px;line-height:30px;font-weight:600}
.service p{position:absolute;left:30px;right:30px;bottom:22px;font-size:14px;line-height:19px}

/* stats */
.stat{position:absolute;top:2170px;width:220px;text-align:center;color:var(--ink)}
.stat svg{display:block;margin:0 auto}
.stat strong{display:block;font-size:38px;font-weight:600;margin-top:12px;line-height:44px}
.stat span{display:block;font-size:16px;font-weight:500;line-height:20px}
.rule{position:absolute;left:89px;width:1022px;height:1px;background:var(--rule)}

/* projects */
.tile{position:absolute}

/* start band */
.band{left:0;top:3176px;width:1200px;height:364px;background:linear-gradient(90deg,rgba(168,25,75,.92),rgba(168,25,75,.96)),linear-gradient(120deg,#7a6a6e,#c9a7a9)}
.band-title{position:absolute;left:0;width:1200px;top:3262px;text-align:center;color:var(--white);font-size:64px;line-height:76px;font-weight:400}
.band-text{position:absolute;left:0;width:1200px;top:3352px;text-align:center;color:var(--white);font-size:15px}

/* testimonials */
.quote{position:absolute;width:460px}
.quote .qmark{position:absolute;left:-46px;top:-30px;font-size:170px;line-height:1;color:#ebe8e9;font-family:Georgia,serif}
.quote .avatar{position:absolute;left:0;top:0;width:50px;height:50px;border-radius:50%;background:linear-gradient(135deg,#d2a368,#5b4a3e);box-shadow:0 2px 6px rgba(0,0,0,.2)}
.quote .stars{position:absolute;left:76px;top:14px;display:flex;gap:4px}
.quote blockquote{position:absolute;left:0;top:68px;width:400px;font-size:22px;line-height:35px;font-weight:500;color:var(--ink)}
.quote .who{position:absolute;left:0;top:216px;font-size:14px;font-weight:600;color:var(--crimson);text-transform:uppercase}
.quote .from{position:absolute;left:0;top:238px;font-size:12px;color:var(--ink)}
.dot{position:absolute;left:1104px;width:10px;height:10px;border-radius:50%;border:1.5px solid var(--muted)}

/* news */
.news{position:absolute;top:4220px;width:502px;height:425px;background:var(--white);box-shadow:0 10px 30px rgba(0,0,0,.12)}
.news .img{position:absolute;left:18px;top:16px;width:466px;height:243px}
.news h4{position:absolute;left:34px;top:278px;width:440px;font-size:17px;line-height:26px;font-weight:600;color:var(--ink)}
.news p{position:absolute;left:34px;top:340px;width:440px;font-size:13px;line-height:21px;color:var(--text)}
.news .more{position:absolute;left:34px;top:392px;font-size:12px;font-weight:600;color:var(--crimson);display:flex;align-items:center;gap:8px}
.interest{position:absolute;left:0;width:1200px;top:4686px;text-align:center;font-size:12px;font-weight:600;color:var(--ink)}
.interest em{font-style:normal;color:var(--crimson)}

/* footer */
.footer{left:0;top:4795px;width:1200px;height:418px;background:var(--footer);color:var(--white)}
.f-mark{left:145px;top:4906px;width:94px;height:94px;border-radius:50%;border:2px solid var(--white)}
.f-name{left:60px;top:5008px;width:264px;text-align:center;font-size:14px;font-weight:600;letter-spacing:4px}
.f-tag{left:60px;top:5032px;width:264px;text-align:center;font-size:12px}
.f-head{position:absolute;top:4880px;font-size:14px;font-weight:600;text-transform:uppercase;letter-spacing:.5px}
.f-links{left:383px;top:4922px;list-style:none;font-size:12px;line-height:31px;text-transform:uppercase}
.f-contact{position:absolute;left:591px;font-size:12px;line-height:20px}
.f-contact svg{position:absolute;left:0;top:3px}
.f-contact div{padding-left:24px}
.f-news{left:854px;top:4922px;width:250px;font-size:12px;line-height:18px}
.f-input{left:854px;top:4977px;width:257px;height:38px;background:var(--white);border-radius:19px;display:flex;align-items:center;padding-left:20px;font-size:12px;color:var(--ink);gap:8px}
.f-send{position:absolute;right:0;top:0;width:40px;height:38px;border-radius:19px;background:var(--crimson);display:flex;align-items:center;justify-content:center}
.social{position:absolute;top:5040px;width:32px;height:32px;border-radius:50%;background:#6c6064;box-shadow:0 0 0 1px rgba(255,255,255,.15)}
.copy{left:0;width:1200px;top:5174px;text-align:center;font-size:13px}
.to-top{left:1138px;top:5141px;width:36px;height:36px;border-radius:50%;background:var(--white);display:flex;align-items:center;justify-content:center}
</style>
</head>
<body>

<!-- Hero -->
<div class="fill hero-photo" role="img" aria-label="Modern office kitchen with long timber table, black chairs and pendant lights"></div>
<div class="brand"><div class="brand-mark"></div><span class="brand-name">ForgeLine Designs</span></div>
<nav class="nav">
  <a class="active">Home</a><a>About Us</a><a>Our Service</a><a>Projects</a><a>Contact</a>
  <svg width="20" height="20" viewBox="0 0 20 20"><circle cx="8" cy="8" r="6.5" fill="none" stroke="#4b4447" stroke-width="2"/><line x1="13" y1="13" x2="19" y2="19" stroke="#4b4447" stroke-width="2"/></svg>
</nav>
<h1 class="abs hero-title">ForgeLine<br>Designs</h1>
<p class="abs hero-text">We are a commercial builder focusing on Fit-out &amp; Renovation works for Offices, schools, retail...</p>
<div class="btn btn-crimson" style="left:89px;top:538px;width:158px;height:45px">Get Started</div>
<div class="fill thumb-a" role="img" aria-label="White kitchen interior with dining chairs"></div>
<div class="fill thumb-b" role="img" aria-label="Bright living room with sofa and pendant lamp"></div>

<!-- About -->
<div class="fill about-panel" role="img" aria-label="Dark diagonal striped panel"></div>
<div class="fill about-ring"></div>
<div class="fill about-photo" role="img" aria-label="Builder levelling timber wall studs"></div>
<h2 class="abs about-title">About Us</h2>
<div class="abs about-text">
  <p>Aenean sollicitudin, lorem quis bibendum auctor, nisi elit sed odio sit amet nibh vulputate cursus a sit amet mauris. Morbi accumsan ipsum velit. Nam nec tellus a odio tincidunt auctor a ornare odio. Sed non mauris vitae erat consequat auctor eu in elit.</p>
  <p style="margin-top:22px">Litora torquent per conubia nostra, pers naeos Mauris in erat justo. Nullam ac urna eu felis</p>
</div>
<div class="btn btn-crimson" style="left:658px;top:1287px;width:154px;height:43px">Learn More</div>

<!-- Services -->
<h2 class="section-title" style="top:1492px">Services</h2>
<div class="service" style="left:0;background:linear-gradient(180deg,#5b6166,#2e3438)" role="img" aria-label="Office corridor fit-out">
  <div class="shade"></div><h3>Fit-out</h3><p>Ltora toruent pernostra per in erat gusto nullam...</p></div>
<div class="service" style="left:297px;background:linear-gradient(180deg,#9aa3ab,#b98a4a 60%,#6b5a48)" role="img" aria-label="Two builders in hard hats reviewing plans">
  <div class="shade"></div><h3>Design<br>and construct</h3><p>Ltora toruent pernostra per in erat gusto nullam...</p></div>
<div class="service" style="left:600px;background:linear-gradient(180deg,#9aa0a6,#3f5a6a 60%,#26343d)" role="img" aria-label="Tower cranes over buildings under construction">
  <div class="shade"></div><h3>Construction</h3><p>Ltora toruent pernostra per in erat gusto nullam...</p></div>
<div class="service" style="left:903px;width:297px;background:linear-gradient(180deg,#8e8a86,#c49a48 50%,#3d3a3a)" role="img" aria-label="Engineer in hard hat holding drawings">
  <div class="shade"></div><h3>Project<br>management</h3><p>Ltora toruent pernostra per in erat gusto nullam...</p></div>

<!-- Stats -->
<div class="stat" style="left:167px">
  <svg width="90" height="56" viewBox="0 0 90 56" fill="none" stroke="#9d1a46" stroke-width="2.5"><circle cx="45" cy="14" r="9"/><path d="M28 50c0-12 8-19 17-19s17 7 17 19z"/><circle cx="18" cy="22" r="7"/><path d="M4 50c0-9 6-15 14-15 4 0 7 1 9 3"/><circle cx="72" cy="22" r="7"/><path d="M86 50c0-9-6-15-14-15-4 0-7 1-9 3"/></svg>
  <strong>400</strong><span>People around<br>australia</span></div>
<div class="stat" style="left:386px">
  <svg width="60" height="60" viewBox="0 0 60 60" fill="none" stroke="#9d1a46" stroke-width="2.5"><circle cx="30" cy="30" r="27"/><circle cx="21" cy="24" r="2" fill="#9d1a46"/><circle cx="39" cy="24" r="2" fill="#9d1a46"/><path d="M18 36c6 8 18 8 24 0"/></svg>
  <strong>183</strong><span>Client forgeline<br>score</span></div>
<div class="stat" style="left:604px">
  <svg width="64" height="60" viewBox="0 0 64 60" fill="none" stroke="#9d1a46" stroke-width="2.5"><circle cx="32" cy="17" r="13"/><path d="M32 9v16M36 12h-6a3 3 0 000 6h4a3 3 0 010 6h-6"/><path d="M4 30l10 22h14l4-10M60 30l-10 22H36l-4-10"/></svg>
  <strong>742</strong><span>National turnover<br>FY2020</span></div>
<div class="stat" style="left:823px">
  <svg width="60" height="62" viewBox="0 0 60 62" fill="none" stroke="#9d1a46" stroke-width="2.5"><path d="M14 22a16 16 0 0132 0z"/><line x1="10" y1="22" x2="50" y2="22"/><circle cx="30" cy="30" r="7"/><path d="M10 60c0-14 9-20 20-20s20 6 20 20z"/></svg>
  <strong>30</strong><span>Years in the<br>inustry</span></div>
<div class="rule" style="top:2441px"></div>

<!-- Projects -->
<h2 class="section-title" style="top:2522px">Our Projects</h2>
<div class="tile" style="left:208px;top:2621px;width:256px;height:227px;background:linear-gradient(180deg,#8a6a4e,#d9d4cc)" role="img" aria-label="Office with curved timber ceiling and booths"></div>
<div class="tile" style="left:474px;top:2621px;width:253px;height:466px;background:linear-gradient(180deg,#7f96aa,#b4874e 60%,#5f7d86)" role="img" aria-label="Tower crane and steel reinforcement"></div>
<div class="tile" style="left:737px;top:2621px;width:255px;height:227px;background:linear-gradient(180deg,#d8cbb0,#6a7a90)" role="img" aria-label="Builder checking timber studs with a level"></div>
<div class="tile" style="left:208px;top:2858px;width:256px;height:229px;background:linear-gradient(180deg,#5a5a5a,#c4bfbb 60%,#9c6b6b)" role="img" aria-label="Meeting room with pink chairs"></div>
<div class="tile" style="left:737px;top:2858px;width:255px;height:229px;background:linear-gradient(160deg,#e7e3df,#c4583a 55%,#a03a2a)" role="img" aria-label="Bricklayer laying red bricks"></div>

<!-- Start my project -->
<div class="fill band" role="img" aria-label="Office lounge interior under a crimson overlay"></div>
<h2 class="band-title">Start My Project</h2>
<p class="band-text">Tell us a little about your project below. No obligations, no catches. Just valuable advice from our experts for you.</p>
<div class="btn btn-white" style="left:522px;top:3396px;width:156px;height:43px">Get Started</div>

<!-- Testimonials -->
<h2 class="section-title" style="top:3638px">Testimonials</h2>
<div class="quote" style="left:136px;top:3734px">
  <div class="qmark">“</div>
  <div class="avatar" role="img" aria-label="Client portrait"></div>
  <div class="stars">
    <svg width="80" height="16" viewBox="0 0 80 16"><g fill="#f0b43c"><path id="s" d="M8 0l2.4 5 5.6.6-4.2 3.8 1.2 5.6L8 12.2 3 15l1.2-5.6L0 5.6 5.6 5z"/><use href="#s" x="16"/><use href="#s" x="32"/><use href="#s" x="48"/></g><use href="#s" x="64" fill="#e8e3d8"/></svg>
  </div>
  <blockquote>"Nam quam nunc blandit velicti luctus pulvinar hendrerit id, lorem maecenas nec odio et ante tincid unt tempus"</blockquote>
  <div class="who">-Daniel Okafor</div><div class="from">from Los Angeles, LA</div>
</div>
<div class="quote" style="left:648px;top:3734px">
  <div class="qmark">“</div>
  <div class="avatar" style="background:linear-gradient(135deg,#9aa6ae,#3f4448)" role="img" aria-label="Client portrait"></div>
  <div class="stars">
    <svg width="80" height="16" viewBox="0 0 80 16"><g fill="#f0b43c"><use href="#s"/><use href="#s" x="16"/><use href="#s" x="32"/><use href="#s" x="48"/></g><use href="#s" x="64" fill="#e8e3d8"/></svg>
  </div>
  <blockquote>"Lorem nunc blandit velicti luctus pulvinar hendrerit id, lorem maece nas nec odio et ante tincid unt tempus"</blockquote>
  <div class="who">-Ellis Navarro</div><div class="from">from New York, NY</div>
</div>
<div class="dot" style="top:3834px;border-color:var(--ink)"></div>
<div class="dot" style="top:3852px"></div>
<div class="dot" style="top:3871px"></div>
<div class="rule" style="top:4078px"></div>

<!-- News -->
<h2 class="section-title" style="top:4143px">Latest News</h2>
<article class="news" style="left:89px">
  <div class="img" style="background:linear-gradient(160deg,#2d3a3a,#7f8d8a 50%,#cfd6d6)" role="img" aria-label="Skyscrapers seen from below"></div>
  <h4>Some news heading goes here with description below...</h4>
  <p>Aenean sollicitudin, lorem quis bibendum auctor, nisi elit sed odio sit amet nibh vulputate cursus a sit amet mauris.</p>
  <div class="more"><svg width="16" height="10" viewBox="0 0 16 10"><path d="M8 0C4 0 1 5 1 5s3 5 7 5 7-5 7-5-3-5-7-5z" fill="#9d1a46"/><circle cx="8" cy="5" r="2" fill="#fff"/></svg>REGISTRIEREN</div>
</article>
<article class="news" style="left:609px">
  <div class="img" style="background:linear-gradient(90deg,#6b5a4c,#c9c3bb 45%,#7f96aa)" role="img" aria-label="Dining room with chandelier and sea view"></div>
  <h4>Some news heading goes here with description below...</h4>
  <p>Aenean sollicitudin, lorem quis bibendum auctor, nisi elit sed odio sit amet nibh vulputate cursus a sit amet mauris.</p>
  <div class="more"><svg width="16" height="10" viewBox="0 0 16 10"><path d="M8 0C4 0 1 5 1 5s3 5 7 5 7-5 7-5-3-5-7-5z" fill="#9d1a46"/><circle cx="8" cy="5" r="2" fill="#fff"/></svg>REGISTRIEREN</div>
</article>
<p class="interest">INTERESTED IN MY? <em>CHECK OUT MORE</em></p>

<!-- Footer -->
<footer class="fill footer"></footer>
<div class="fill f-mark"></div>
<div class="abs f-name" style="color:#fff">ForgeLine Designs</div>
<div class="abs f-tag" style="color:#fff">Building with peace of mind</div>

<div class="f-head" style="left:383px;color:#fff">Quick Links</div>
<ul class="abs f-links" style="color:#fff"><li>Home</li><li>About Us</li><li>Our Service</li><li>Projects</li><li>Contact Us</li></ul>

<div class="f-head" style="left:591px;color:#fff">Contact Info</div>
<div class="f-contact" style="top:4926px;color:#fff">
  <svg width="14" height="10" viewBox="0 0 14 10"><rect x="0.5" y="0.5" width="13" height="9" fill="none" stroke="#fff"/><path d="M1 1l6 5 6-5" fill="none" stroke="#fff"/></svg>
  <div>Email:<br>info@example.com</div></div>
<div class="f-contact" style="top:4986px;color:#fff">
  <svg width="13" height="13" viewBox="0 0 24 24"><path d="M6.6 10.8a15 15 0 006.6 6.6l2.2-2.2c.3-.3.7-.4 1-.2 1.1.4 2.3.6 3.6.6.6 0 1 .4 1 1V20c0 .6-.4 1-1 1A17 17 0 013 4c0-.6.4-1 1-1h3.5c.6 0 1 .4 1 1 0 1.3.2 2.5.6 3.6.1.3 0 .7-.2 1z" fill="#fff"/></svg>
  <div>Phone:<br>123-456-7890</div></div>
<div class="f-contact" style="top:5048px;color:#fff">
  <svg width="11" height="15" viewBox="0 0 12 16"><path d="M6 0a6 6 0 00-6 6c0 4.5 6 10 6 10s6-5.5 6-10a6 6 0 00-6-6z" fill="#fff"/><circle cx="6" cy="6" r="2" fill="#5a4e52"/></svg>
  <div>Office Location:<br>Some address line goes here</div></div>

<div class="f-head" style="left:854px;top:4882px;color:#fff">Newsletter</div>
<p class="abs f-news" style="color:#fff">Subscribe to our email address to get the latest news.</p>
<div class="abs f-input">
  <svg width="12" height="9" viewBox="0 0 14 10"><rect x="0.5" y="0.5" width="13" height="9" fill="none" stroke="#8a8486"/><path d="M1 1l6 5 6-5" fill="none" stroke="#8a8486"/></svg>
  Enter Your Email...
  <div class="f-send"><svg width="16" height="16" viewBox="0 0 16 16"><path d="M15 1L1 7l5 2 2 6z" fill="#fff"/></svg></div>
</div>
<div class="social" style="left:858px"></div>
<div class="social" style="left:899px"></div>
<div class="social" style="left:941px"></div>

<p class="abs copy" style="color:#fff">© Copyright 2020 &nbsp;|&nbsp; All Rights Reserved</p>
<div class="abs to-top"><svg width="12" height="14" viewBox="0 0 12 14"><path d="M6 13V2M1 6l5-5 5 5" fill="none" stroke="#4b4447" stroke-width="2"/></svg></div>

</body>
</html>
```